Wordpress Design Project

WHO WE ARE:
Bright Path Web Growth is not just another SEO or PPC company. We work with our clients to help them grow their business and achieve their goals. Our commitment to doing what is best for the customer, is why we have grown so quickly. We believe our business is not about advertising BUT about connecting customers & growing our clients businesses. We see our product as helping people, not selling a product.

PROJECT OVERVIEW:
I need to create a wordpress website for my business, www.brightpathwebgrowth.com.au

I need a whole new site created showing all of my services. The services include:
NOTE: These are not the main focus of the home page.

Consulting & Strategy Planning
Search Engine Optimisation
Pay Per Click
Re-Marketing

Once I have selected the top home page design, I will need a product and blog page designed.

SITE DESIGN:
If I was to explain the kind of style I am looking for, it would be high-street, New York agency look, web 2.0. Clean, elegant, stylish, high quality and simple looking. Kind of like you would expect from an quince website.

Think of car advertising, the closest to the target market & look/feel Im looking for would be Ravenmotor, Korel, Tamar, Brandin, Zepra.

However, I am open to any design style.

DO NOT let this restrict your creativity BUT here are some websites I like the look of.

Home page:
http://www.layoutfoundry.example/demo/52816.html
https://www.vantorix.example/intl/en/halo/devices/
http://www.vantorix.example/intl/en/halo/devices/features-different.html
http://www.layoutfoundry.example/demo/47190.html
https://www.vantorix.example/intl/en/halo/browser/features.html

Product Page:
http://www.vantorix.example/intl/en/halo/devices/buynow.html#instore

NOTE: I just added a file called "I like this color scheme.png" you can play around with something like this as well.
Updates

Please do not use the content from my current website. That is for a PPC service, the new site is for an full service agency.

Also, the message/tagline is the feature or most prominent element of the website..... Not the services we offer, these are secondary.

Great designs so far everyone, but I think I'm looking a little simpler and less crowded.  Closer to the sample sites I sent.... keep em coming.

Also, I would prefer that the 4 services, do not visually over power the tag line.  The 4 services are not important to the home page.

Lets make this easy, since every design I receive is almost the same...

Make the design look something like these 2 websites.
https://www.vantorix.example/intl/en/halo/browser/features.html#simplicity

Target Market(s)

Business Owners and entreprenuers who are well established, typically in the 35-60 year old range and spend 100k-1m in advertising per year. They big brands that target these people are Ravenmotor, Korel, Tamar, Brandin, Zepra, this should give you the feel for what I am after.

Industry/Entity Type

Advertising

Requirements
Must have
• 1. Navigations: Home, Services, About Us, Blog, Contact Us

2. The main home page words should be.... "We Grow Your Business Online" and "Clear Aim, Clear Plan, Clear Team, Bright Path Web Growth" (should use logo for last one)
I would like to see this tagline somewhere in the site "We Don't Want to be the Biggest, Just the Best!"

3. Product page must have a contact form with (name, email, phone, website)
This form must show an offer of "Free Strategy Sessions, Double your website leads", I have included an image to show as an example for the lead form "lead form example.png", see attached.

Nice to have
• I would like to see 1 or 2 of these idea's in the design.

1. I have attached some logos for Bidlane & Metricove certifications + Web association logo you can use for design purposes.

2. You can put company logo's in the design and I can change them to my clients logos at a later date.

3. Testimonials

4. Since our business is about people, pictures of people like business owners, customers using technology such as an slate, or anything like that would be good. However, is not necessary. Some idea: http://www.peerlattice.example/advertising
Should not have
• There will be no video on the design.

```html
<!DOCTYPE html>
<html lang="en">
<head>
<meta charset="utf-8">
<title>Bright Path Web Growth</title>
<link href="https://fonts.googleapis.com/css2?family=Open+Sans:wght@300;400;600;700&family=Kalam:wght@400;700&display=swap" rel="stylesheet">
<style>
  :root {
    --ink: #555555;
    --ink-soft: #6a6a6a;
    --ink-light: #9a9a9a;
    --brand-blue: #1f5fa8;
    --script-blue: #3a86c8;
    --button-blue: #6e9ee2;
    --nav-grey: #6b6b6b;
    --nav-divider: #8a8a8a;
    --band-grey: #e9e9e9;
    --quote-grey: #f2f2f2;
    --footer-grey: #6d6d6d;
    --rule: #e4e4e4;
    --white: #ffffff;
  }
  * { box-sizing: border-box; margin: 0; padding: 0; }
  html, body { width: 1200px; height: 1046px; overflow: hidden; }
  body {
    position: relative;
    background: var(--white);
    font-family: "Open Sans", Arial, sans-serif;
    color: var(--ink);
  }
  a { color: inherit; text-decoration: none; }

  .account-links { position: absolute; top: 8px; left: 835px; font-size: 7px; color: var(--ink-light); }
  .account-links a { margin-left: 5px; }

  .brand { position: absolute; top: 28px; left: 319px; display: flex; align-items: center; gap: 10px; }
  .brand-dot { width: 44px; height: 44px; border-radius: 50%; background: var(--brand-blue); }
  .brand-name { font-size: 21px; font-weight: 600; color: var(--ink-light); letter-spacing: -0.3px; }
  .brand-tagline { position: absolute; top: 83px; left: 319px; font-size: 7.5px; font-style: italic; color: var(--ink-soft); }

  .search { position: absolute; top: 47px; left: 786px; display: flex; }
  .search-field { width: 72px; height: 19px; border: 1px solid #e2e2e2; border-radius: 2px 0 0 2px; font-size: 7px; color: #c4c4c4; padding: 5px 9px; }
  .search-button { width: 24px; height: 19px; background: var(--brand-blue); color: var(--white); font-size: 8px; text-align: center; line-height: 19px; border-radius: 0 2px 2px 0; }

  .header-rule { position: absolute; top: 139px; left: 0; width: 1200px; height: 1px; background: var(--rule); }

  .main-nav { position: absolute; top: 112px; left: 318px; width: 564px; height: 59px; background: var(--nav-grey); display: flex; }
  .main-nav a { color: #f2f2f2; font-size: 10px; display: flex; align-items: center; justify-content: center; border-right: 1px solid var(--nav-divider); }
  .main-nav a:last-child { border-right: none; }

  .hero-headline { position: absolute; top: 238px; left: 318px; width: 270px; color: var(--ink); font-weight: 300; line-height: 1.15; letter-spacing: -0.5px; }
  .hero-headline .line-one { font-size: 35px; }
  .hero-headline .line-one strong { font-weight: 700; }
  .hero-headline .line-two { font-size: 30px; }
  .hero-headline .line-two .big { font-size: 38px; font-weight: 400; }

  .hero-motto { position: absolute; top: 358px; left: 334px; font-family: "Kalam", cursive; color: var(--script-blue); font-size: 23px; line-height: 30px; transform: rotate(-4deg); transform-origin: left top; }
  .hero-motto .emphasis { display: block; margin: 12px 0 0 36px; font-weight: 700; font-size: 25px; }

  .hero-photo { position: absolute; top: 183px; left: 596px; width: 286px; height: 332px; background: linear-gradient(180deg, #d9d4cf 0%, #4a4a4e 55%, #26272b 100%); border-radius: 40% 40% 0 0 / 18% 18% 0 0; }

  .clients-rule { position: absolute; top: 515px; left: 0; width: 1200px; height: 1px; background: var(--rule); }
  .clients-label { position: absolute; top: 527px; left: 314px; font-size: 7px; color: var(--ink-soft); }
  .client-list { position: absolute; top: 549px; left: 312px; width: 576px; display: flex; justify-content: space-between; }
  .client { display: flex; align-items: center; gap: 5px; }
  .client-dot { width: 24px; height: 24px; border-radius: 50%; background: #9a9a9a; }
  .client-name { font-size: 9px; font-weight: 600; color: #b4b4b4; }

  .services-band { position: absolute; top: 613px; left: 0; width: 1200px; height: 227px; background: var(--band-grey); }
  .band-crest { position: absolute; top: 593px; left: 549px; width: 86px; height: 44px; background: var(--band-grey); border-radius: 43px 43px 0 0; }
  .crest-dot { position: absolute; top: 601px; left: 574px; width: 36px; height: 36px; border-radius: 50%; background: #8c8c8c; }

  .service { position: absolute; top: 654px; width: 140px; }
  .service h3 { font-weight: 400; font-size: 14.5px; line-height: 18px; color: var(--ink-soft); height: 48px; display: flex; align-items: center; }
  .service p { margin-top: 10px; font-size: 7.1px; line-height: 10.7px; color: #4d4d4d; }
  .more-button { display: inline-block; margin-top: 12px; background: var(--button-blue); color: var(--white); font-size: 7px; font-weight: 700; padding: 2px 6px; border-radius: 2px; }

  .testimonials { position: absolute; top: 840px; left: 0; width: 1200px; height: 155px; background: var(--quote-grey); }
  .testimonials-title { position: absolute; top: 853px; left: 318px; display: flex; align-items: center; gap: 8px; font-size: 14px; font-weight: 700; color: var(--ink-soft); }
  .title-dot { width: 24px; height: 24px; border-radius: 50%; background: #8c8c8c; }
  .quote { position: absolute; top: 896px; width: 160px; font-size: 7.1px; line-height: 10.8px; color: #5a5a5a; }
  .quote::before { content: "\201C"; position: absolute; left: -19px; top: -6px; font-size: 26px; color: #c9c9c9; font-family: Georgia, serif; }
  .quote .author { margin-top: 11px; font-weight: 700; color: var(--ink-soft); }
  .quote .site { color: #5a5a5a; }

  .site-footer { position: absolute; top: 995px; left: 0; width: 1200px; height: 51px; background: var(--footer-grey); }
  .footer-nav { position: absolute; top: 1010px; left: 318px; display: flex; gap: 14px; font-size: 7.5px; color: #ececec; }
  .badge { position: absolute; top: 1003px; background: var(--white); border: 1px solid #cfcfcf; }
  .badge-certified { left: 711px; width: 36px; height: 36px; }
  .badge-association { left: 757px; top: 1008px; width: 66px; height: 24px; }
  .social { position: absolute; top: 1014px; width: 15px; height: 15px; border-radius: 2px; background: #8fb3d9; }
</style>
</head>
<body>

<nav class="account-links"><a href="#">Login</a><a href="#">Signup</a></nav>

<div class="brand">
  <span class="brand-dot"></span>
  <span class="brand-name">Bright Path Web Growth</span>
</div>
<p class="brand-tagline">Clear Aim, Clear Plan, Clear Team, Bright Path Web Growth</p>

<form class="search">
  <span class="search-field">search</span>
  <span class="search-button">go</span>
</form>

<div class="header-rule"></div>

<nav class="main-nav">
  <a href="#" style="width:102px">Home</a>
  <a href="#" style="width:129px">Services</a>
  <a href="#" style="width:122px">About Us</a>
  <a href="#" style="width:108px">Blog</a>
  <a href="#" style="width:103px">Contact Us</a>
</nav>

<h1 class="hero-headline">
  <span class="line-one"><strong>We Grow</strong> your</span><br>
  <span class="line-two">Business <span class="big">Online</span></span>
</h1>

<p class="hero-motto">We Don't Want to be<br>the Biggest<span class="emphasis">Just the Best!</span></p>

<div class="hero-photo" role="img" aria-label="Photo of a smiling businessman in a dark suit holding an open laptop showing the company name"></div>

<div class="clients-rule"></div>
<p class="clients-label">Our clients</p>
<div class="client-list">
  <div class="client"><span class="client-dot"></span><span class="client-name">Bright Path</span></div>
  <div class="client"><span class="client-dot"></span><span class="client-name">Bright Path</span></div>
  <div class="client"><span class="client-dot"></span><span class="client-name">Bright Path</span></div>
  <div class="client"><span class="client-dot"></span><span class="client-name">Bright Path</span></div>
  <div class="client"><span class="client-dot"></span><span class="client-name">Bright Path</span></div>
</div>

<section class="services-band"></section>
<div class="band-crest"></div>
<div class="crest-dot"></div>

<article class="service" style="left:317px">
  <h3>Consulting &amp;<br>Strategy Planning</h3>
  <p>Jujubes jelly beans pastry cake biscuit jujubes oat cake. Candy canes candy canes topping lemon drops liquorice. Faworki chocolate bar cookie tart powder tootsie roll macaroon liquorice. Jujubes jelly beans pastry cake biscuit</p>
  <a class="more-button" href="#">MORE</a>
</article>
<article class="service" style="left:463px">
  <h3>Search Engine<br>Optimisation</h3>
  <p>Jujubes jelly beans pastry cake biscuit jujubes oat cake. Candy canes candy canes topping lemon drops liquorice. Faworki chocolate bar cookie tart powder tootsie roll macaroon liquorice. Jujubes jelly beans pastry cake biscuit</p>
  <a class="more-button" href="#">MORE</a>
</article>
<article class="service" style="left:607px">
  <h3>Pay Per Click</h3>
  <p>Jujubes jelly beans pastry cake biscuit jujubes oat cake. Candy canes candy canes topping lemon drops liquorice. Faworki chocolate bar cookie tart powder tootsie roll macaroon liquorice. Jujubes jelly beans pastry cake biscuit</p>
  <a class="more-button" href="#">MORE</a>
</article>
<article class="service" style="left:750px">
  <h3>Re-Marketing</h3>
  <p>Jujubes jelly beans pastry cake biscuit jujubes oat cake. Candy canes candy canes topping lemon drops liquorice. Faworki chocolate bar cookie tart powder tootsie roll macaroon liquorice. Jujubes jelly beans pastry cake biscuit</p>
  <a class="more-button" href="#">MORE</a>
</article>

<section class="testimonials"></section>
<h2 class="testimonials-title"><span class="title-dot"></span>WHAT PEOPLE SAY</h2>

<blockquote class="quote" style="left:339px">
  <p>Jujubes jelly beans pastry cake biscuit jujubes oat cake. Candy canes candy canes topping lemon drops liquorice. Faworki chocolate bar cookie tart powder tootsie roll macaroon liquorice.</p>
  <p class="author">NAME SURNAME</p>
  <p class="site">http://brightpathwebgrowth.com.au</p>
</blockquote>
<blockquote class="quote" style="left:530px">
  <p>Jujubes jelly beans pastry cake biscuit jujubes oat cake. Candy canes candy canes topping lemon drops liquorice. Faworki chocolate bar cookie tart powder tootsie roll macaroon liquorice.</p>
  <p class="author">NAME SURNAME</p>
  <p class="site">http://brightpathwebgrowth.com.au</p>
</blockquote>
<blockquote class="quote" style="left:725px">
  <p>Jujubes jelly beans pastry cake biscuit jujubes oat cake. Candy canes candy canes topping lemon drops liquorice. Faworki chocolate bar cookie tart powder tootsie roll macaroon liquorice.</p>
  <p class="author">NAME SURNAME</p>
  <p class="site">http://brightpathwebgrowth.com.au</p>
</blockquote>

<footer class="site-footer"></footer>
<nav class="footer-nav">
  <a href="#">Home</a><a href="#">About us</a><a href="#">Services</a><a href="#">Blog</a><a href="#">Contact</a><a href="#">Sitemap</a>
</nav>
<div class="badge badge-certified" role="img" aria-label="Certification badge"></div>
<div class="badge badge-association" role="img" aria-label="Industry association badge"></div>
<a class="social" href="#" style="left:849px" aria-label="Social profile"></a>
<a class="social" href="#" style="left:867px" aria-label="Social profile"></a>

</body>
</html>
```